Looking for an amazing business card for a thriving DJ business

We need a business card design for a DJ company based in South Florida. The DJ company specializes in weddings, parties, bar mitzvahs, corporate events, proms, and reunions. We are looking for a modern, simple business card design. The card should state DJ Marlow K.
Updates

The name on the card should be DJ Marlow K

Industry/Entity Type

Entertainment Industry

Contact Information for Business Card

DJ Marlow K
512.447.2086
atxdjmarlowk@quellmail.com
https://www.facebook.com/DjMarlowK/
https://www.instagram.com/djmarlow.k/
www.djmarlowk.net

Font styles to use
Serif
Sans Serif

Requirements
Must have
• My business card has to be awesome.
Should not have
• The card has to have personality.

```html
<!DOCTYPE html>
<html lang="en">
<head>
<meta charset="utf-8">
<title>DJ Marlow K — Business Card</title>
<link rel="stylesheet" href="https://fonts.googleapis.com/css2?family=Strait&display=swap">
<style>
  :root {
    --paper: #ffffff;
    --night-top: #8c2656;
    --night-mid: #5a2548;
    --night-bottom: #321a3b;
    --rule-start: #4d2446;
    --rule-end: #26173a;
    --ink-title: #3e1d3d;
    --ink-contact: #4c2446;
  }
  * { margin: 0; padding: 0; box-sizing: border-box; }
  html, body {
    width: 1200px;
    height: 720px;
    overflow: hidden;
    background: var(--paper);
  }
  .card {
    position: relative;
    width: 1200px;
    height: 720px;
    background: var(--paper);
    font-family: "Strait", sans-serif;
  }
  .night-panel {
    position: absolute;
    left: 40px;
    top: 40px;
    width: 368px;
    height: 631px;
    background: linear-gradient(135deg, var(--night-top) 0%, var(--night-mid) 45%, var(--night-bottom) 100%);
  }
  .brand-name {
    position: absolute;
    left: 593px;
    top: 124px;
    font-size: 70px;
    font-weight: 400;
    line-height: 1;
    color: var(--ink-title);
    letter-spacing: 0.5px;
    white-space: nowrap;
  }
  .divider {
    position: absolute;
    left: 408px;
    top: 242px;
  }
  .contact-list {
    position: absolute;
    left: 486px;
    top: 307px;
    list-style: none;
    color: var(--ink-contact);
    font-size: 32px;
    line-height: 52.7px;
    white-space: nowrap;
  }
</style>
</head>
<body>
  <main class="card">
    <div class="night-panel" role="img" aria-label="Starry night sky with scattered glowing stars"></div>

    <h1 class="brand-name">DJ Marlow K</h1>

    <svg class="divider" width="738" height="12" viewBox="0 0 738 12" aria-hidden="true">
      <defs>
        <linearGradient id="rule-fade" x1="0" x2="1" y1="0" y2="0">
          <stop offset="0" stop-color="var(--rule-start)"/>
          <stop offset="1" stop-color="var(--rule-end)"/>
        </linearGradient>
      </defs>
      <rect width="738" height="12" fill="url(#rule-fade)"/>
    </svg>

    <ul class="contact-list">
      <li class="contact-phone">512.447.2086</li>
      <li class="contact-email">atxdjmarlowk@quellmail.com</li>
      <li class="contact-social">www.frendloop.com/DjMarlowK/</li>
      <li class="contact-gallery">www.picturely.com/djmarlow.k/</li>
      <li class="contact-website">www.djmarlowk.net</li>
    </ul>
  </main>
</body>
</html>
```